Labels for fruit liqueur bottles

We are looking for a visual identity based on our logo, for fruit liqueur labels. To date, we have different liqueurs such as: lemon liqueur, orange liqueurs, mandarin liqueurs, grapefruit liqueurs. We will then create other liqueurs such as strawberry, apple or even apricot. Our goal is to have a single visual that we can adapt in different colors depending on the fruit used.

On the label there should be:
the logo
homemade
the name of the fruit (which can be changed depending on the product)
swiss-made
50cl
21°

Colors

Designer to choose colors to be used in the design.

Requirements
Must have
• a visual of liquor bottle labels, with the possibility of changing the background colors, depending on the fruit used
Nice to have
• something modern and nice to look at. We must be able to read the basic fruit in the blink of an eye. it is also possible to have a black or white or colored label background.

```html
<!DOCTYPE html>
<html lang="en">
<head>
<meta charset="utf-8">
<title>Casa Belvino – Lemon Liqueur Label</title>
<link rel="stylesheet" href="https://fonts.googleapis.com/css2?family=Arimo:wght@700&family=Lobster&family=Oswald:wght@500&family=Alegreya:wght@500&family=Courier+Prime&display=swap">
<style>
  :root {
    --bg: #ffffff;
    --brand: #e5532c;
    --fruit: #efaa24;
    --fruit-soft: #f6c55a;
    --fruit-pale: #fbe7bd;
    --ink: #1f1f1f;
  }
  * { margin: 0; padding: 0; box-sizing: border-box; }
  html, body {
    width: 1200px;
    height: 1067px;
    overflow: hidden;
    background: var(--bg);
  }
  .canvas {
    position: relative;
    width: 1200px;
    height: 1067px;
  }
  .label {
    position: absolute;
    left: 250px;
    top: 140px;
    width: 380px;
    height: 790px;
    text-align: center;
  }
  .brand {
    position: absolute;
    left: 0;
    top: 0;
    width: 100%;
  }
  .brand-mark {
    display: block;
    width: 88px;
    height: 88px;
    margin: 0 auto;
    border-radius: 50%;
    background: var(--brand);
  }
  .brand-name {
    margin-top: 16px;
    font-family: "Arimo", sans-serif;
    font-weight: 700;
    font-size: 31px;
    letter-spacing: -0.4px;
    color: var(--brand);
    line-height: 1;
  }
  .brand-tagline {
    margin-top: 4px;
    font-family: "Arimo", sans-serif;
    font-weight: 700;
    font-size: 15px;
    color: var(--brand);
    line-height: 1;
  }
  .fruit-illustration {
    position: absolute;
    left: 62px;
    top: 180px;
    width: 256px;
    height: 296px;
    border-radius: 50% 46% 48% 50%;
    background: radial-gradient(circle at 62% 66%, var(--fruit-soft), var(--fruit-pale) 70%, var(--bg) 100%);
  }
  .homemade {
    position: absolute;
    left: 0;
    top: 494px;
    width: 100%;
    font-family: "Lobster", cursive;
    font-size: 31px;
    color: var(--ink);
    line-height: 1;
  }
  .fruit-name {
    position: absolute;
    left: 0;
    top: 530px;
    width: 100%;
    font-family: "Oswald", sans-serif;
    font-weight: 500;
    font-size: 126px;
    letter-spacing: 4px;
    line-height: 1;
    color: var(--fruit);
  }
  .rule {
    position: absolute;
    border-top: 3px dotted var(--ink);
  }
  .rule-top { top: 664px; left: 14px; width: 352px; }
  .rule-bottom { top: 730px; left: 82px; width: 216px; }
  .product-type {
    position: absolute;
    left: 0;
    top: 670px;
    width: 100%;
    font-family: "Alegreya", serif;
    font-weight: 500;
    font-size: 44px;
    line-height: 1.2;
    color: var(--ink);
  }
  .specs {
    position: absolute;
    left: 18px;
    top: 748px;
    width: 344px;
    display: flex;
    justify-content: space-between;
    align-items: baseline;
    font-family: "Courier Prime", monospace;
    color: var(--ink);
  }
  .specs .volume, .specs .strength { font-size: 24px; }
  .specs .origin { font-size: 18px; }
  .side-illustration {
    position: absolute;
    left: 690px;
    top: 500px;
    width: 330px;
    height: 390px;
    border-radius: 52% 48% 50% 50%;
    background: radial-gradient(circle at 62% 66%, var(--fruit-soft), var(--fruit-pale) 68%, var(--bg) 100%);
  }
</style>
</head>
<body>
  <main class="canvas">
    <section class="label">
      <header class="brand">
        <span class="brand-mark"></span>
        <p class="brand-name">CASA BELVINO</p>
        <p class="brand-tagline">liqueur de fruits</p>
      </header>
      <div class="fruit-illustration" role="img" aria-label="Line drawing of a whole lemon with a leaf and a halved lemon in golden yellow"></div>
      <p class="homemade">Homemade</p>
      <h1 class="fruit-name">LEMON</h1>
      <span class="rule rule-top"></span>
      <p class="product-type">Liqueur</p>
      <span class="rule rule-bottom"></span>
      <footer class="specs">
        <span class="volume">50cl</span>
        <span class="origin">Swiss-Made</span>
        <span class="strength">21°</span>
      </footer>
    </section>
    <div class="side-illustration" role="img" aria-label="Large line drawing of a lemon with leaf and a lemon half in golden yellow"></div>
  </main>
</body>
</html>
```